Bright Arch Group business card

Bright Arch Group is the parent company of Bright Arch Building, Bright Arch Plumbing and Bright Arch Renovating. We require a sophisticated business card that covers all aspects of the building and plumbing space without using told or construction items.

Industry/Entity Type

Construction Company

Contact Information for Business Card

Gareth Pimley
Director
0472915083
gareth@brightarch.com.au
Www.brightarch.com.au

Font styles to use
Serif
Sans Serif

Colors
3176b5
ffce3e
0692cd
34a7d8
fbee3e
faa54b

Requirements
Must have
• Logo on front
• Logo and details on rear.
Nice to have
• Maybe water mark or shadow effect with logo
Should not have
• Tools or any construction associated items

```html
<!DOCTYPE html>
<html lang="en">
<head>
<meta charset="utf-8">
<title>Bright Arch Group – Business Card</title>
<link rel="stylesheet" href="https://fonts.googleapis.com/css2?family=Arimo:wght@400;700&display=swap">
<style>
  :root {
    --page-bg: #e9eaec;
    --card-blue-light: #5cc3e8;
    --card-blue-deep: #34a7d8;
    --accent-orange: #faa54b;
    --stripe-orange: #f7931e;
    --paper-white: #ffffff;
    --ink-dark: #1d1d1f;
    --ink-light: #ffffff;
  }
  * { box-sizing: border-box; margin: 0; padding: 0; }
  html, body {
    width: 1200px; height: 1200px; overflow: hidden;
    background: var(--page-bg);
    font-family: "Arimo", Arial, sans-serif;
  }
  .sheet {
    width: 1200px; height: 1200px;
    display: flex; flex-direction: column; align-items: center; justify-content: center;
    gap: 60px;
  }
  .card {
    position: relative;
    width: 840px; height: 480px;
    overflow: hidden;
    box-shadow: 0 10px 24px rgba(0,0,0,0.18);
  }

  /* Back of card */
  .card-back {
    background: linear-gradient(135deg, var(--card-blue-light), var(--card-blue-deep));
    display: flex; flex-direction: column; align-items: center; justify-content: center;
    gap: 22px;
    color: var(--ink-light);
  }
  .brand-back {
    display: flex; align-items: center; gap: 16px;
    font-size: 40px; font-weight: 400; letter-spacing: 0.04em;
  }
  .brand-back .brand-dot {
    width: 22px; height: 22px; border-radius: 50%; background: var(--ink-light);
  }
  .card-back .web { font-size: 20px; letter-spacing: 0.02em; }

  /* Front of card */
  .card-front { background: var(--paper-white); }
  .card-front .panel {
    position: absolute; inset: 0; width: 100%; height: 100%;
  }
  .brand-front {
    position: absolute; left: 60px; top: 190px;
    display: flex; align-items: center; gap: 14px;
    color: var(--ink-dark);
  }
  .brand-front .brand-dot {
    width: 18px; height: 18px; border-radius: 50%; background: var(--accent-orange);
    flex: none;
  }
  .brand-front .brand-name {
    display: flex; flex-direction: column; align-items: center;
    font-size: 30px; font-weight: 400; letter-spacing: 0.14em; line-height: 1.2;
    text-transform: uppercase;
  }
  .details {
    position: absolute; left: 560px; top: 150px;
    color: var(--ink-light);
  }
  .details .name { font-size: 40px; font-weight: 400; line-height: 1; }
  .details .role { font-size: 18px; margin-top: 4px; }
  .contact-list { list-style: none; margin-top: 34px; display: flex; flex-direction: column; gap: 14px; }
  .contact-list li { display: flex; align-items: center; gap: 10px; font-size: 17px; }
  .contact-list svg { width: 16px; height: 16px; flex: none; }
</style>
</head>
<body>
<main class="sheet">

  <section class="card card-back" aria-label="Card back">
    <div class="brand-back"><span class="brand-dot"></span>Bright Arch Group</div>
    <p class="web">www.brightarch.com.au</p>
  </section>

  <section class="card card-front" aria-label="Card front">
    <svg class="panel" viewBox="0 0 840 480" preserveAspectRatio="none" aria-hidden="true">
      <defs>
        <linearGradient id="blueFill" x1="0" y1="0" x2="1" y2="1">
          <stop offset="0" stop-color="#4dbbe3"/>
          <stop offset="1" stop-color="#2fa3d6"/>
        </linearGradient>
      </defs>
      <polygon points="530,0 840,0 840,480 300,480" fill="url(#blueFill)"/>
      <line x1="530" y1="0" x2="300" y2="480" stroke="var(--stripe-orange)" stroke-width="9"/>
    </svg>

    <div class="brand-front">
      <span class="brand-dot"></span>
      <span class="brand-name"><span>Bright Arch</span><span>Group</span></span>
    </div>

    <div class="details">
      <h1 class="name">Gareth Pimley</h1>
      <p class="role">Director</p>
      <ul class="contact-list">
        <li>
          <svg viewBox="0 0 16 16" aria-hidden="true"><path fill="var(--accent-orange)" d="M3.6 1.2l2.2 2.6-1.3 1.7c.9 2 2.3 3.5 4.2 4.5l1.7-1.3 2.6 2.2-1.2 2.3C7.2 13.7 2.4 8.9 1.3 2.4z"/></svg>
          0472915083
        </li>
        <li>
          <svg viewBox="0 0 16 16" aria-hidden="true"><rect x="1" y="3" width="14" height="10" rx="1" fill="var(--accent-orange)"/><path d="M1.5 3.8L8 9l6.5-5.2" stroke="#fff" stroke-width="1.2" fill="none"/></svg>
          gareth@brightarch.com.au
        </li>
        <li>
          <svg viewBox="0 0 16 16" aria-hidden="true"><g fill="none" stroke="var(--accent-orange)" stroke-width="1.4"><circle cx="8" cy="8" r="6.3"/><ellipse cx="8" cy="8" rx="2.8" ry="6.3"/><path d="M1.7 8h12.6"/></g></svg>
          www.brightarch.com.au
        </li>
      </ul>
    </div>
  </section>

</main>
</body>
</html>
```